Modern, cutting edge crypto trading website.

I need a single-page website design, approximate 4-5 pages. I have included a screenshot of the inside of the current application for some reference for what it currently looks like. This is the public side of the application for not logged in users.

I am currently thinking about 3-5 sections of the page.
Menu at top is optional, these could be the sections of the site.
1. Above the fold cool, grabbing stuff.
2. What problem does this solve
3. Additional benefits
4. Pricing
5. Open to ideas! Well it's all open to ideas if you have ideas.

I am nervous about hiring designers, I am open to a further discussion for more work for additional money but I have to LIKE your design. So this could be considered a trial. I would like to continue to design the application itself and match everything together!

I really like the trendkite website.

Competitor websites:
https://7pillars.example/
https://www.trendkite.example/

Target Market(s)

Adults 25-50 mostly male,

Number of Pages Required

4 page

Colors

Designer to choose colors to be used in the design.

Requirements
Must have
• Modern design, clean lines, professional.
Nice to have
• Fun SVG stuff. Not for this price, but in the future.
Should not have
• Should not be cluttered OR too spacey. Quorble's website has too much open space sometimes.

```html
<!DOCTYPE html>
<html lang="en">
<head>
<meta charset="utf-8">
<title>Pulse Vector — Crypto Trading</title>
<link rel="stylesheet" href="https://fonts.googleapis.com/css2?family=Montserrat:wght@300;400;500;600;700;800&display=swap">
<style>
:root{
  --blue:#1f78c4;
  --blue-deep:#0c3f9a;
  --blue-navy:#0a2a7a;
  --cyan:#2aa6e0;
  --ink:#1c1c1c;
  --muted:#6f6f6f;
  --pale:#e9f1f9;
  --white:#ffffff;
  --line:#e4e8ee;
}
*{box-sizing:border-box;margin:0;padding:0}
html,body{width:1200px;height:4823px;overflow:hidden}
body{position:relative;font-family:'Montserrat',sans-serif;color:var(--ink);background:var(--white)}
.abs{position:absolute}
.btn{position:absolute;display:flex;align-items:center;justify-content:center;height:50px;border-radius:25px;background:linear-gradient(90deg,var(--cyan),var(--blue));color:var(--white);font-weight:600;font-size:17px;text-decoration:none}
.kicker{font-weight:600;font-size:20px}
.heading{font-size:40px;font-weight:300;color:var(--blue);letter-spacing:.5px}
.heading b{font-weight:700}
.body{font-size:14px;line-height:27px;color:var(--muted)}
.brand{display:flex;align-items:center;gap:10px;font-size:20px;font-weight:400;color:var(--blue)}
.brand .mark{width:38px;height:38px;background:var(--blue);border-radius:4px}
.nav{position:absolute;top:30px;left:622px;display:flex;gap:28px;font-size:13px;color:var(--white);font-weight:500;align-items:center}
.nav .login{background:var(--white);color:var(--blue);border-radius:22px;padding:11px 24px;font-weight:600;font-size:15px;margin-left:2px}
.art{position:absolute}
.step{position:absolute;width:270px;text-align:center}
.step .icon{width:100px;height:100px;border-radius:50%;background:linear-gradient(135deg,var(--cyan),var(--blue-deep));margin:0 auto 40px}
.step h3{font-size:17px;font-weight:600;margin-bottom:12px}
.step p{font-size:14px;line-height:27px;color:var(--muted)}
.item{position:absolute;left:78px;display:flex;gap:28px;font-size:14px;line-height:27px;color:var(--muted)}
.item svg{flex:none;margin-top:6px}
.card{position:absolute;width:334px;height:352px;background:var(--white);border-radius:6px;box-shadow:0 6px 24px rgba(0,0,0,.08);padding:36px 34px}
.card .icon{width:90px;height:90px;border-radius:50%;background:linear-gradient(135deg,var(--cyan),var(--blue-deep));border:4px solid #d9e8f6}
.card h4{font-size:20px;font-weight:600;margin:40px 0 10px}
.card p{font-size:14px;line-height:27px;color:var(--muted)}
.card .more{position:absolute;right:34px;bottom:26px;font-size:14px;color:var(--blue);text-decoration:underline}
.card .more::after{content:"";display:inline-block;margin-left:8px;border-left:7px solid var(--blue);border-top:5px solid transparent;border-bottom:5px solid transparent}
.plan{position:absolute;background:var(--white);border:1px solid var(--line)}
.plan.featured{background:#f4f4f4;border:none}
.plan .head{position:absolute;top:0;left:0;right:0}
.plan .tier{position:absolute;right:30px;color:var(--white);font-size:19px;font-weight:400}
.plan .price{position:absolute;right:30px;color:var(--white);font-size:46px;font-weight:700}
.plan .dot{position:absolute;left:88px;width:50px;height:50px;border-radius:50%;background:#dfe7f3}
.plan ul{position:absolute;left:28px;list-style:none}
.plan li{display:flex;gap:16px;align-items:center;font-size:14px;color:var(--muted);height:42px}
.plan .btn{left:24px;width:174px}
.cta-line{position:absolute;left:0;width:1200px;text-align:center}
.fcol{position:absolute;top:4604px}
.fcol h5{font-size:15px;font-weight:300;color:var(--blue);margin-bottom:22px}
.fcol h5 b{font-weight:600}
.fcol p{font-size:14px;color:#555;height:31px;display:flex;align-items:center;gap:16px}
.social{display:flex;gap:8px;margin-top:10px}
.social span{width:40px;height:40px;border-radius:50%;background:var(--blue-deep)}
</style>
</head>
<body>

<!-- HERO -->
<svg class="abs" style="left:0;top:0" width="1200" height="690" viewBox="0 0 1200 690">
  <defs><linearGradient id="heroG" x1="0" y1="0" x2="1" y2="1"><stop offset="0" stop-color="#2aa6e0"/><stop offset=".6" stop-color="#1565b8"/><stop offset="1" stop-color="#0a2a7a"/></linearGradient></defs>
  <path d="M420 0 H1200 V672 C1120 690 1000 660 930 570 C860 480 760 470 660 400 C520 300 600 180 500 100 C450 60 420 30 420 0Z" fill="url(#heroG)"/>
</svg>
<div class="brand abs" style="left:75px;top:22px"><span class="mark"></span>Pulse Vector</div>
<nav class="nav"><span>HOME</span><span>ABOUT</span><span>BENEFITS</span><span>PRICING</span><span>CONTACT</span><span class="login">LOGIN</span></nav>
<div class="art" role="img" aria-label="Isometric crypto trading platform with laptop and server stacks" style="left:495px;top:110px;width:640px;height:480px;border-radius:50%;background:radial-gradient(circle,#7fd6f5 0%,#2a9be0 45%,rgba(31,120,196,0) 72%)"></div>
<h1 class="abs" style="left:75px;top:272px;font-size:40px;font-weight:800;color:var(--blue);letter-spacing:.5px">CRYPTO TRADING</h1>
<div class="abs" style="left:75px;top:325px;font-size:30px;font-weight:400">Pulse Vector</div>
<p class="abs body" style="left:77px;top:372px;width:340px">Lorem Ipsum is simply dummy text of the printing and typesetting industry.</p>
<a class="btn" style="left:77px;top:443px;width:178px">GET STARTED</a>
<svg class="abs" style="left:78px;top:641px" width="100" height="18">
  <g fill="none" stroke="#1f78c4" stroke-width="1.5"><circle cx="8" cy="9" r="6"/><circle cx="50" cy="9" r="6"/><circle cx="70" cy="9" r="6"/><circle cx="90" cy="9" r="6"/></g>
  <circle cx="29" cy="9" r="7" fill="#0c3f9a"/>
</svg>

<!-- HOW TO GET STARTED -->
<div class="abs kicker" style="left:0;width:1200px;text-align:center;top:718px">Pulse Vector</div>
<h2 class="abs heading" style="left:0;width:1200px;text-align:center;top:750px">HOW TO <b>GET STARTED</b></h2>
<div class="step" style="left:176px;top:840px"><div class="icon"></div><h3>Connect Exchange</h3><p>Lorem Ipsum is simply dummy text of the printing and typesetting is industry Lorem Ipsum</p></div>
<div class="step" style="left:466px;top:840px"><div class="icon"></div><h3>Create or Select Strategy</h3><p>Lorem Ipsum is simply dummy text of the printing and typesetting is industry Lorem Ipsum</p></div>
<div class="step" style="left:756px;top:840px"><div class="icon"></div><h3>Automatically Rebalance</h3><p>Lorem Ipsum is simply dummy text of the printing and typesetting is industry Lorem Ipsum</p></div>

<!-- ABOUT -->
<svg class="abs" style="left:0;top:1170px" width="620" height="700" viewBox="0 0 620 700">
  <defs><linearGradient id="paleL" x1="0" y1="0" x2="0" y2="1"><stop offset="0" stop-color="#e6f1fb"/><stop offset="1" stop-color="#f4f7fb"/></linearGradient></defs>
  <path d="M0 60 C120 -20 300 0 380 80 C470 170 560 270 500 400 C430 540 160 520 70 580 C30 610 10 650 0 690Z" fill="url(#paleL)"/>
</svg>
<div class="art" role="img" aria-label="Crypto network illustration with laptop and linked server stacks" style="left:112px;top:1305px;width:360px;height:360px;border-radius:50%;background:radial-gradient(circle at 45% 40%,#1a6fd0,#0a2a7a)"></div>
<div class="abs kicker" style="left:676px;top:1240px">About Us</div>
<h2 class="abs heading" style="left:674px;top:1274px">PULSE <b>VECTOR</b></h2>
<p class="abs body" style="left:678px;top:1336px;width:400px">Lorem Ipsum is simply dummy text of the printing and typesetting industry. Lorem Ipsum has been the industry's standard dummy text ever.</p>
<p class="abs body" style="left:678px;top:1431px;width:400px">Lorem Ipsum is simply dummy text of the printing and typesetting industry. Lorem Ipsum has been the industry's standard dummy text ever since the 1500s, when an unknown printer took a galley.</p>
<a class="btn" style="left:681px;top:1557px;width:173px">LEARN MORE</a>

<!-- PROBLEM WE SOLVE -->
<svg class="abs" style="left:600px;top:1975px" width="600" height="420" viewBox="0 0 600 420">
  <defs><linearGradient id="paleR" x1="0" y1="0" x2="1" y2="0"><stop offset="0" stop-color="#f4f7fb"/><stop offset="1" stop-color="#e3eef9"/></linearGradient></defs>
  <path d="M600 10 C480 0 380 30 300 60 C160 110 0 150 10 260 C20 360 200 340 360 360 C470 372 540 400 600 412Z" fill="url(#paleR)"/>
</svg>
<div class="art" role="img" aria-label="Central coin platform connected to isometric blocks" style="left:745px;top:1906px;width:344px;height:344px;border-radius:50%;background:radial-gradient(circle at 45% 35%,#1a6fd0,#0a2a7a)"></div>
<div class="abs kicker" style="left:78px;top:1876px">What We Do</div>
<h2 class="abs heading" style="left:76px;top:1908px">PROBLEM <b>WE SOLVE</b></h2>
<div class="item" style="top:1986px"><svg width="20" height="16" viewBox="0 0 20 16" fill="none" stroke="#1f78c4" stroke-width="1.8"><path d="M1 8h16M11 2l6 6-6 6"/></svg><span>Lorem Ipsum is simply dummy text of the<br>printing and typesetting industry.</span></div>
<div class="item" style="top:2062px"><svg width="20" height="16" viewBox="0 0 20 16" fill="none" stroke="#1f78c4" stroke-width="1.8"><path d="M1 8h16M11 2l6 6-6 6"/></svg><span>Lorem Ipsum is simply dummy text of the<br>printing &amp; typesetting industry.</span></div>
<div class="item" style="top:2138px"><svg width="20" height="16" viewBox="0 0 20 16" fill="none" stroke="#1f78c4" stroke-width="1.8"><path d="M1 8h16M11 2l6 6-6 6"/></svg><span>Lorem Ipsum is simply dummy text of the<br>printing and typesetting industry.</span></div>
<div class="item" style="top:2214px"><svg width="20" height="16" viewBox="0 0 20 16" fill="none" stroke="#1f78c4" stroke-width="1.8"><path d="M1 8h16M11 2l6 6-6 6"/></svg><span>Lorem Ipsum is simply dummy text of the<br>printing and typesetting industry.</span></div>
<a class="btn" style="left:77px;top:2303px;width:172px">LEARN MORE</a>

<!-- BENEFITS -->
<svg class="abs" style="left:0;top:2410px" width="1200" height="1030" viewBox="0 0 1200 1030">
  <defs><linearGradient id="blueB" x1="0" y1="1" x2="1" y2="0"><stop offset="0" stop-color="#3aa7e2"/><stop offset=".5" stop-color="#1f78c4"/><stop offset="1" stop-color="#1668b8"/></linearGradient></defs>
  <path d="M1200 40 C1000 -10 720 -20 500 30 C300 80 190 200 170 400 C150 600 170 760 300 880 C430 990 700 1010 900 990 C1060 975 1150 950 1200 920Z" fill="url(#blueB)"/>
</svg>
<h2 class="abs heading" style="left:0;width:1200px;text-align:center;top:2532px;color:var(--white)">ADDITIONAL <b>BENEFITS</b></h2>
<p class="abs" style="left:0;width:1200px;text-align:center;top:2590px;font-size:14px;line-height:27px;color:var(--white)">Lorem Ipsum is simply dummy text of the printing and<br>typesetting industry.</p>
<div class="card" style="left:256px;top:2681px"><div class="icon"></div><h4>Lorem Ipsum Text</h4><p>Lorem ipsum is simply dummy text of the printing and typesetting is industry Lorem Ipsum</p><span class="more">Read More</span></div>
<div class="card" style="left:610px;top:2681px"><div class="icon"></div><h4>Lorem Ipsum Text</h4><p>Lorem ipsum is simply dummy text of the printing and typesetting is industry Lorem Ipsum</p><span class="more">Read More</span></div>
<div class="card" style="left:256px;top:3059px"><div class="icon"></div><h4>Lorem Ipsum Text</h4><p>Lorem ipsum is simply dummy text of the printing and typesetting is industry Lorem Ipsum</p><span class="more">Read More</span></div>
<div class="card" style="left:610px;top:3059px"><div class="icon"></div><h4>Lorem Ipsum Text</h4><p>Lorem ipsum is simply dummy text of the printing and typesetting is industry Lorem Ipsum</p><span class="more">Read More</span></div>

<!-- PRICING -->
<div class="abs kicker" style="left:0;width:1200px;text-align:center;top:3478px">Pulse Vector</div>
<h2 class="abs heading" style="left:0;width:1200px;text-align:center;top:3510px">OUR <b>PRICING</b></h2>
<svg width="0" height="0" style="position:absolute"><defs><linearGradient id="planG" x1="0" y1="0" x2="1" y2="1"><stop offset="0" stop-color="#2aa6e0"/><stop offset=".5" stop-color="#1565b8"/><stop offset="1" stop-color="#0a2a7a"/></linearGradient></defs></svg>

<div class="plan" style="left:131px;top:3660px;width:313px;height:487px">
  <svg class="head" width="313" height="180" viewBox="0 0 313 180"><path d="M0 0H313V180 C250 180 215 150 190 100 C160 40 90 20 0 20Z" fill="url(#planG)"/></svg>
  <span class="tier" style="top:36px">Starter</span><span class="price" style="top:62px">$22</span><span class="dot" style="top:88px"></span>
  <ul style="top:204px">
    <li><svg width="16" height="14" viewBox="0 0 20 16" fill="none" stroke="#1f78c4" stroke-width="2"><path d="M1 8h16M11 2l6 6-6 6"/></svg>Lorem Ipsum is simply text</li>
    <li><svg width="16" height="14" viewBox="0 0 20 16" fill="none" stroke="#1f78c4" stroke-width="2"><path d="M1 8h16M11 2l6 6-6 6"/></svg>Lorem Ipsum is.</li>
    <li><svg width="16" height="14" viewBox="0 0 20 16" fill="none" stroke="#1f78c4" stroke-width="2"><path d="M1 8h16M11 2l6 6-6 6"/></svg>Lorem Ipsum is text</li>
    <li><svg width="16" height="14" viewBox="0 0 20 16" fill="none" stroke="#1f78c4" stroke-width="2"><path d="M1 8h16M11 2l6 6-6 6"/></svg>Lorem Ipsum is simply text</li>
    <li><svg width="16" height="14" viewBox="0 0 20 16" fill="none" stroke="#1f78c4" stroke-width="2"><path d="M1 8h16M11 2l6 6-6 6"/></svg>Lorem Ipsum is text</li>
  </ul>
  <a class="btn" style="top:412px">GET STARTED</a>
</div>

<div class="plan featured" style="left:444px;top:3609px;width:312px;height:562px">
  <svg class="head" width="312" height="180" viewBox="0 0 312 180"><path d="M0 0H312V180 C250 180 215 150 190 100 C160 40 90 20 0 20Z" fill="url(#planG)"/></svg>
  <span class="tier" style="top:36px">Advanced</span><span class="price" style="top:62px">$37</span><span class="dot" style="top:88px"></span>
  <ul style="top:213px">
    <li><svg width="16" height="14" viewBox="0 0 20 16" fill="none" stroke="#1f78c4" stroke-width="2"><path d="M1 8h16M11 2l6 6-6 6"/></svg>Lorem Ipsum is text</li>
    <li><svg width="16" height="14" viewBox="0 0 20 16" fill="none" stroke="#1f78c4" stroke-width="2"><path d="M1 8h16M11 2l6 6-6 6"/></svg>Lorem Ipsum is simply text</li>
    <li><svg width="16" height="14" viewBox="0 0 20 16" fill="none" stroke="#1f78c4" stroke-width="2"><path d="M1 8h16M11 2l6 6-6 6"/></svg>Lorem Ipsum is.</li>
    <li><svg width="16" height="14" viewBox="0 0 20 16" fill="none" stroke="#1f78c4" stroke-width="2"><path d="M1 8h16M11 2l6 6-6 6"/></svg>Lorem Ipsum is text</li>
    <li><svg width="16" height="14" viewBox="0 0 20 16" fill="none" stroke="#1f78c4" stroke-width="2"><path d="M1 8h16M11 2l6 6-6 6"/></svg>Lorem Ipsum is simply text</li>
    <li><svg width="16" height="14" viewBox="0 0 20 16" fill="none" stroke="#1f78c4" stroke-width="2"><path d="M1 8h16M11 2l6 6-6 6"/></svg>Lorem Ipsum is text</li>
  </ul>
  <a class="btn" style="top:463px">GET STARTED</a>
</div>

<div class="plan" style="left:756px;top:3660px;width:313px;height:487px">
  <svg class="head" width="313" height="180" viewBox="0 0 313 180"><path d="M0 0H313V180 C250 180 215 150 190 100 C160 40 90 20 0 20Z" fill="url(#planG)"/></svg>
  <span class="tier" style="top:36px">Pro</span><span class="price" style="top:62px">$75</span><span class="dot" style="top:88px"></span>
  <ul style="top:204px">
    <li><svg width="16" height="14" viewBox="0 0 20 16" fill="none" stroke="#1f78c4" stroke-width="2"><path d="M1 8h16M11 2l6 6-6 6"/></svg>Lorem Ipsum is simply text</li>
    <li><svg width="16" height="14" viewBox="0 0 20 16" fill="none" stroke="#1f78c4" stroke-width="2"><path d="M1 8h16M11 2l6 6-6 6"/></svg>Lorem Ipsum is.</li>
    <li><svg width="16" height="14" viewBox="0 0 20 16" fill="none" stroke="#1f78c4" stroke-width="2"><path d="M1 8h16M11 2l6 6-6 6"/></svg>Lorem Ipsum is text</li>
    <li><svg width="16" height="14" viewBox="0 0 20 16" fill="none" stroke="#1f78c4" stroke-width="2"><path d="M1 8h16M11 2l6 6-6 6"/></svg>Lorem Ipsum is simply text</li>
    <li><svg width="16" height="14" viewBox="0 0 20 16" fill="none" stroke="#1f78c4" stroke-width="2"><path d="M1 8h16M11 2l6 6-6 6"/></svg>Lorem Ipsum is text</li>
  </ul>
  <a class="btn" style="top:412px">GET STARTED</a>
</div>

<!-- CTA -->
<span class="abs" style="left:575px;top:4230px;width:50px;height:50px;background:var(--blue);border-radius:6px"></span>
<div class="cta-line" style="top:4310px;font-size:26px;font-weight:300;color:var(--cyan)">Ready To Get Started?</div>
<div class="cta-line" style="top:4345px;font-size:40px;font-weight:700;color:var(--blue)">Join Us Right Now!</div>
<p class="cta-line" style="top:4407px;font-size:15px;color:var(--muted)">Lorem Ipsum is simply dummy text of the printing industry.</p>
<a class="btn" style="left:515px;top:4447px;width:171px">GET STARTED</a>

<!-- FOOTER -->
<div class="abs" style="left:75px;top:4567px;width:1050px;height:1px;background:var(--line)"></div>
<svg class="abs" style="left:0;top:4630px" width="170" height="193" viewBox="0 0 170 193"><path d="M0 10 C60 30 90 90 110 140 C125 175 150 190 170 193H0Z" fill="#1f78c4"/></svg>
<svg class="abs" style="left:1130px;top:4720px" width="70" height="103" viewBox="0 0 70 103"><path d="M70 0 C30 10 0 50 10 103H70Z" fill="#1f78c4"/></svg>
<div class="brand abs" style="left:94px;top:4646px"><span class="mark"></span>Pulse Vector</div>
<p class="abs" style="left:100px;top:4700px;width:125px;text-align:center;font-size:14px;line-height:22px;color:#555">©Pulse Vector -2019 All rights reserved.</p>
<div class="fcol" style="left:348px"><h5>SITE<b>MAP</b></h5><p>Home</p><p>About</p><p>Benefits</p><p>Pricing</p><p>Contact</p></div>
<div class="fcol" style="left:614px"><h5>LEGAL<b>INFO</b></h5><p>Terms of use</p><p>Personal information</p><p>Return policy</p><p>Partner agreement</p></div>
<div class="fcol" style="left:880px"><h5>CONTACT<b>US</b></h5>
  <p><svg width="18" height="18" viewBox="0 0 24 24" fill="#1f78c4"><path d="M6.6 10.8a15 15 0 0 0 6.6 6.6l2.2-2.2c.3-.3.7-.4 1-.2 1.1.4 2.3.6 3.6.6.6 0 1 .4 1 1V20c0 .6-.4 1-1 1A17 17 0 0 1 3 4c0-.6.4-1 1-1h3.5c.6 0 1 .4 1 1 0 1.3.2 2.5.6 3.6.1.3 0 .7-.2 1z"/></svg>123 456 7890</p>
  <p><svg width="18" height="14" viewBox="0 0 24 18" fill="#1f78c4"><path d="M0 0h24v18H0z"/><path d="M1 1l11 8 11-8" fill="none" stroke="#fff" stroke-width="2"/></svg>hello@pulsevector.example</p>
  <div class="social"><span></span><span></span><span></span><span></span></div>
</div>

</body>
</html>
```